Bluestone Advisory & Mgmt - Professional Business Cards

Hi!

I am a Real Estate Developer and Construction Consultant.

I have a lot of inspiration from previous designs and would be open to using the attached Designs as a starting point. I would like to see these styles incorporated into your designs.

I really need professional business card to go with it that includes my important info.

Look forward to seeing your designs!.

Target Market(s)

My Target market are building owners, lawyers, consultants.

Industry/Entity Type

Real Estate Development

Contact Information for Business Card

My Name: Dorian Pelkey
My Title: Principle
Company Name: Bluestone Advisory & Mgmt, LLC
Address: 348 West 71st Street, 9th FL New York, NY 10010
Mobile: 917.806.3971
Website: bam-hvx.example

Font styles to use
Serif
Sans Serif

Colors

Designer to choose colors to be used in the design.

Requirements
Must have
• Must incorporate the logo attached or have new that looks similar.
• Must use professional font that will be seen and judged by wealthy land owners and developers.
• Must incorporate some of the color green.
Should not have
• Photo's or pictures of people or buildings of any kind.

```html
<!DOCTYPE html>
<html lang="en">
<head>
<meta charset="utf-8">
<title>Bluestone Advisory &amp; Mgmt - Business Cards</title>
<link rel="stylesheet" href="https://fonts.googleapis.com/css2?family=Oswald:wght@400;500;600&family=Raleway:wght@400;500&display=swap">
<style>
  :root {
    --page-bg: #e9e9e7;
    --card-dark: #46463f;
    --card-light: #f7f7f7;
    --brand-green: #35a86a;
    --text-grey: #6f6f6f;
    --watermark: #ececec;
    --logo-grey: #9a8f8f;
  }
  html, body {
    margin: 0;
    padding: 0;
    width: 1200px;
    height: 1021px;
    overflow: hidden;
    background: var(--page-bg);
  }
  .sheet {
    position: relative;
    width: 1200px;
    height: 1021px;
  }
  .card {
    position: absolute;
    left: 220px;
    width: 760px;
    height: 434px;
    box-shadow: 0 6px 18px rgba(0,0,0,0.18);
    overflow: hidden;
  }
  .card--back {
    top: 56px;
    background: var(--card-dark);
  }
  .card--front {
    top: 530px;
    background: linear-gradient(135deg, #fbfbfb 0%, var(--card-light) 55%, #ececec 100%);
  }
  .brand-mark {
    position: absolute;
    right: 56px;
    bottom: 52px;
    text-align: left;
    font-family: "Raleway", sans-serif;
    font-weight: 400;
    color: var(--brand-green);
  }
  .brand-mark__primary {
    display: block;
    font-size: 64px;
    line-height: 1;
    letter-spacing: 1px;
  }
  .brand-mark__secondary {
    display: block;
    font-size: 27px;
    line-height: 1.3;
    letter-spacing: 2px;
  }
  .watermark-name {
    position: absolute;
    left: 0;
    right: 0;
    top: 30px;
    text-align: center;
    font-family: "Raleway", sans-serif;
    font-weight: 500;
    font-size: 150px;
    line-height: 1;
    color: var(--watermark);
    letter-spacing: -2px;
    user-select: none;
  }
  .info {
    position: absolute;
    font-family: "Oswald", sans-serif;
    color: var(--text-grey);
  }
  .person {
    left: 60px;
    top: 208px;
    width: 220px;
    text-align: right;
  }
  .person__name {
    font-size: 27px;
    font-weight: 600;
    text-transform: uppercase;
    line-height: 1.1;
  }
  .person__title {
    font-size: 19px;
    font-weight: 400;
    text-transform: uppercase;
    line-height: 1.2;
  }
  .person__rule {
    display: block;
    width: 42px;
    height: 3px;
    background: var(--text-grey);
    margin: 26px 0 14px auto;
  }
  .person__web {
    font-size: 19px;
  }
  .company {
    left: 318px;
    top: 264px;
    font-size: 19px;
    line-height: 1.25;
  }
  .company__name {
    text-transform: uppercase;
    font-weight: 400;
  }
  .company__highlight {
    color: var(--brand-green);
    font-weight: 500;
  }
  .company__contact {
    margin-top: 14px;
  }
</style>
</head>
<body>
<main class="sheet">
  <section class="card card--back" aria-label="Card back">
    <div class="brand-mark">
      <span class="brand-mark__primary">Bluestone</span>
      <span class="brand-mark__secondary">Advisory &amp; Mgmt</span>
    </div>
  </section>

  <section class="card card--front" aria-label="Card front">
    <div class="watermark-name" aria-hidden="true">Bluestone</div>

    <div class="info person">
      <div class="person__name">Dorian Pelkey</div>
      <div class="person__title">Principle</div>
      <span class="person__rule"></span>
      <div class="person__web">www.bam-hvx.example</div>
    </div>

    <div class="info company">
      <div class="company__name"><span class="company__highlight">Bluestone</span> Advisory &amp; Mgmt, LLC</div>
      <div>348 West 71st Street, 9th FL</div>
      <div>New York, NY 10010</div>
      <div class="company__contact">917.806.3971</div>
      <div>dorian@bam-hvx.example</div>
    </div>
  </section>
</main>
</body>
</html>
```